Post Card Design Bright Path Youth

We need a postcard design that will be mailed to all residents offering free pickups of donated clothing. Our foundation is called Bright Path Youth, we are a nonprofit charitable organization that provides meals and medical services to children in need in Honduras. Collecting unwanted second-hand clothing generates revenue that helps fund the mission and programs run by our foundation. We would like to offer our pickup services to everyone who has any unwanted reusable clothing.

```html
<!DOCTYPE html>
<html lang="en">
<head>
<meta charset="utf-8">
<title>Bright Path Youth Postcard</title>
<link href="https://fonts.googleapis.com/css2?family=Jost:wght@400;500;600&family=Montserrat:wght@800;900&display=swap" rel="stylesheet">
<style>
:root{
  --bg:#c8c8c8;
  --green:#7dc242;
  --green-deep:#6cb233;
  --magenta:#e6138a;
  --blue:#1e8fd5;
  --yellow:#fcc419;
  --white:#ffffff;
  --stamp:#ececec;
  --rule:#e4e4e4;
}
*{margin:0;padding:0;box-sizing:border-box}
html,body{width:1200px;height:2184px;overflow:hidden}
body{background:var(--bg);position:relative;font-family:'Jost',sans-serif}
.card{position:absolute;left:156px;width:888px;height:591px;overflow:hidden;box-shadow:0 10px 24px rgba(0,0,0,.18)}
.card-front{top:420px;background:var(--magenta)}
.card-back{top:1130px;background:var(--white)}
.front-field{position:absolute;left:17px;top:17px;right:17px;bottom:17px;background:radial-gradient(circle at 45% 35%,#86c94c,var(--green) 60%,var(--green-deep))}
.abs{position:absolute}
.brand-name{font-weight:600;color:var(--white);font-size:38px;left:0;width:544px;text-align:center;top:168px;line-height:1}
.headline-top{font-family:'Montserrat',sans-serif;font-weight:900;color:var(--white);font-size:42px;left:0;width:544px;text-align:center;top:262px;line-height:1}
.headline-main{font-family:'Montserrat',sans-serif;font-weight:900;color:var(--white);font-size:66px;left:26px;width:454px;text-align:center;top:326px;line-height:1;letter-spacing:1px}
.tagline{left:26px;top:408px;width:452px;height:59px;background:var(--blue);border-radius:14px;color:var(--white);font-size:22px;line-height:26px;text-align:center;padding-top:4px}
.contact-row{left:30px;top:512px;display:flex;align-items:center;color:var(--white);font-weight:600;font-size:15px}
.contact-row .item{display:flex;align-items:center;gap:10px;margin-right:26px}
.icon{width:22px;height:22px;flex:none}
.photo-ring{left:493px;top:129px;width:348px;height:348px}
.back-art{left:0;top:0;width:888px;height:591px}
.section-title{left:32px;top:54px;font-family:'Montserrat',sans-serif;font-weight:900;font-size:27px;line-height:1}
.section-title .w1{color:var(--yellow)}
.section-title .w2{color:var(--blue)}
.title-rule{left:32px;top:93px;width:92px;height:2px;background:var(--yellow)}
.body-copy{left:32px;top:110px;width:440px;color:var(--white);font-size:17.5px;line-height:22px}
.body-copy p+p{margin-top:22px}
.back-photos{left:31px;top:336px;width:440px;height:182px}
.back-brand{left:580px;top:146px;width:170px;text-align:center;color:var(--green);font-weight:600;font-size:19px;line-height:1}
.stamp-box{left:776px;top:98px;width:75px;height:75px;background:var(--stamp)}
.address-line{left:622px;width:231px;height:1px;background:var(--rule)}
.back-contacts{left:650px;top:478px;color:var(--blue);font-weight:600}
.back-contacts .item{display:flex;align-items:center;gap:10px;height:26px}
.back-contacts .phone{font-size:19px}
.back-contacts .small{font-size:14px}
</style>
</head>
<body>

<section class="card card-front" aria-label="Postcard front">
  <div class="front-field" role="img" aria-label="Faint background photo of a smiling child tinted green">
    <div class="abs brand-name">Bright Path Youth</div>
    <div class="abs headline-top">LET’S MAKE A</div>
    <div class="abs headline-main">DIFFERENCE</div>
    <div class="abs tagline">Free Pickup of Your Donated Clothing<br>Right from Your Doorstep</div>

    <svg class="abs photo-ring" viewBox="0 0 348 348">
      <circle cx="174" cy="174" r="172" fill="var(--blue)"/>
      <circle cx="174" cy="174" r="164" fill="var(--green)"/>
      <circle cx="174" cy="174" r="161" fill="var(--magenta)"/>
      <circle cx="174" cy="174" r="156" fill="#b9a98e" role="img" aria-label="Photo of a girl receiving a donation bag from a volunteer"/>
    </svg>

    <div class="abs contact-row">
      <span class="item">
        <svg class="icon" viewBox="0 0 22 22"><circle cx="11" cy="11" r="10" fill="var(--yellow)"/><path d="M7 6.5c.6-.6 1.4-.5 1.8.2l.8 1.4c.3.5.2 1-.2 1.4l-.5.5c.5 1.2 1.6 2.3 2.8 2.8l.5-.5c.4-.4 1-.5 1.4-.2l1.4.8c.7.4.8 1.2.2 1.8l-.6.6c-.7.7-1.8.8-2.7.3-2.2-1.2-4-3-5.2-5.2-.5-.9-.4-2 .3-2.7z" fill="var(--white)"/></svg>
        (555) 014-2087
      </span>
      <span class="item">
        <svg class="icon" viewBox="0 0 22 22"><circle cx="11" cy="11" r="10" fill="var(--yellow)"/><rect x="5.5" y="7" width="11" height="8" rx="1" fill="none" stroke="var(--white)" stroke-width="1.4"/><path d="M5.8 7.5 11 11.5l5.2-4" fill="none" stroke="var(--white)" stroke-width="1.4"/></svg>
        info@brightpathyouth.org
      </span>
      <span class="item">
        <svg class="icon" viewBox="0 0 22 22"><circle cx="11" cy="11" r="10" fill="var(--yellow)"/><g fill="none" stroke="var(--white)" stroke-width="1.3"><circle cx="11" cy="11" r="5.5"/><ellipse cx="11" cy="11" rx="2.4" ry="5.5"/><path d="M5.5 11h11"/></g></svg>
        brightpathyouth.org
      </span>
    </div>
  </div>
</section>

<section class="card card-back" aria-label="Postcard back">
  <svg class="abs back-art" viewBox="0 0 888 591">
    <circle cx="141" cy="290" r="434" fill="var(--blue)"/>
    <circle cx="141" cy="290" r="422" fill="var(--yellow)"/>
    <circle cx="141" cy="290" r="406" fill="var(--green)"/>
    <rect x="0" y="0" width="141" height="591" fill="var(--green)"/>
  </svg>

  <div class="abs section-title"><span class="w1">OUR</span> <span class="w2">WORK</span></div>
  <div class="abs title-rule"></div>
  <div class="abs body-copy">
    <p>We offer free pickups of your unwanted reusable clothing. Every bag you donate helps fund meals and medical care for children in Honduras.</p>
    <p>Bright Path Youth is a nonprofit charity. Second-hand clothing you no longer need becomes revenue for our programs. Call or email us to book a free pickup, and we will collect your donation right from your door.</p>
  </div>

  <svg class="abs back-photos" viewBox="0 0 440 182">
    <circle cx="91" cy="91" r="90" fill="var(--magenta)"/>
    <circle cx="91" cy="91" r="87" fill="#6f6a64" role="img" aria-label="Photo of a woman cooking a meal over an open fire"/>
    <circle cx="229" cy="91" r="90" fill="var(--blue)"/>
    <circle cx="229" cy="91" r="87" fill="#7d7a72" role="img" aria-label="Photo of volunteers walking with children in a village"/>
    <circle cx="349" cy="91" r="90" fill="var(--yellow)"/>
    <circle cx="349" cy="91" r="87" fill="#8a8780" role="img" aria-label="Photo of women preparing food in a community kitchen"/>
  </svg>

  <div class="abs back-brand">Bright Path Youth</div>
  <div class="abs stamp-box"></div>
  <div class="abs address-line" style="top:262px"></div>
  <div class="abs address-line" style="top:321px"></div>
  <div class="abs address-line" style="top:380px"></div>

  <div class="abs back-contacts">
    <div class="item phone">
      <svg class="icon" viewBox="0 0 22 22"><circle cx="11" cy="11" r="10" fill="var(--green)"/><path d="M7 6.5c.6-.6 1.4-.5 1.8.2l.8 1.4c.3.5.2 1-.2 1.4l-.5.5c.5 1.2 1.6 2.3 2.8 2.8l.5-.5c.4-.4 1-.5 1.4-.2l1.4.8c.7.4.8 1.2.2 1.8l-.6.6c-.7.7-1.8.8-2.7.3-2.2-1.2-4-3-5.2-5.2-.5-.9-.4-2 .3-2.7z" fill="var(--white)"/></svg>
      (555) 014-2087
    </div>
    <div class="item small">
      <svg class="icon" viewBox="0 0 22 22"><circle cx="11" cy="11" r="10" fill="var(--green)"/><rect x="5.5" y="7" width="11" height="8" rx="1" fill="none" stroke="var(--white)" stroke-width="1.4"/><path d="M5.8 7.5 11 11.5l5.2-4" fill="none" stroke="var(--white)" stroke-width="1.4"/></svg>
      info@brightpathyouth.org
    </div>
    <div class="item small">
      <svg class="icon" viewBox="0 0 22 22"><circle cx="11" cy="11" r="10" fill="var(--green)"/><g fill="none" stroke="var(--white)" stroke-width="1.3"><circle cx="11" cy="11" r="5.5"/><ellipse cx="11" cy="11" rx="2.4" ry="5.5"/><path d="M5.5 11h11"/></g></svg>
      brightpathyouth.org
    </div>
  </div>
</section>

</body>
</html>
```